new incubator startup Plattform

I need a flyer for a business presentation.
Please insert the text ideas from following the attachment.

We are a new incubator, accelerator and co working space for startups. The innovation platform that unites global companies with high tech expertise and the best of Austrian knowhow. Our focus is in AI, Blockchain and e-commerce.
We are a neutral platform moderating an in-depth and curated collaboration between our partners from the industry and young tech companies. Our network of investment firms and mentors further helps the growth of tech companies. Our home is Vienna, a hub of business, engineering, and groundbreaking inventions.

Focus:
AI, Blockchain, e-commerce

Cases
Startup Idea
You have a disruptive idea that needs an accelerator/incubator program

Business Challenge
You want to solve an business problem but do not own an idea

Mature startup Idea
You Have a Disruptive idea that needs a direct commercialization

Benefits
Market and Investor Acces
Direct access to all Partners

Training and Tools

Mentor and Network Muscle
We can link you to many domains like Sales, Marketing, Aftersales, IT und HR.
Experiences Senior and University mentors.
With all Partners as your first potential customer.

```html
<!DOCTYPE html>
<html lang="en">
<head>
<meta charset="utf-8">
<title>Incubator Flyer – AI, Blockchain, e-commerce</title>
<link href="https://fonts.googleapis.com/css2?family=Mulish:wght@300;400;700;800&display=swap" rel="stylesheet">
<style>
  :root {
    --page-bg: #e8e5e0;
    --paper: #ffffff;
    --night: #05070f;
    --night-blue: #0b3a7a;
    --glow-blue: #2a7fe0;
    --teal: #127a98;
    --teal-dark: #0b5670;
    --ink: #2f2f2f;
    --gold-dark: #ac6404;
    --gold-light: #c8930a;
    --white: #ffffff;
  }
  * { margin: 0; padding: 0; box-sizing: border-box; }
  html, body { width: 956px; height: 1200px; overflow: hidden; }
  body { background: var(--page-bg); font-family: "Mulish", sans-serif; position: relative; }

  .flyer {
    position: absolute; left: 54px; top: 0;
    width: 848px; height: 1200px;
    background: var(--paper); overflow: hidden;
  }
  .hero {
    position: absolute; left: 0; top: 0; width: 848px; height: 240px;
    background: radial-gradient(ellipse at 70% 55%, var(--glow-blue) 0%, var(--night-blue) 35%, var(--night) 75%);
  }
  .hero-wave { position: absolute; left: 0; top: 140px; width: 848px; height: 100px; }
  .hero-title {
    position: absolute; left: 41px; top: 108px; transform: translateY(-100%);
    color: var(--white); font-weight: 700; font-size: 34px; letter-spacing: 0.2px;
    white-space: nowrap; line-height: 1;
  }

  .connectors { position: absolute; left: 0; top: 0; width: 848px; height: 800px; }

  .case-bubble {
    position: absolute; width: 252px; height: 252px; border-radius: 50%;
    background: linear-gradient(160deg, var(--teal) 0%, var(--teal-dark) 100%);
    color: var(--white); font-weight: 700; font-size: 21.5px; line-height: 1.27;
    display: flex; align-items: center; justify-content: center; text-align: center;
    padding: 0 18px;
  }
  .bubble-startup { left: 137px; top: 157px; }
  .bubble-challenge { left: 540px; top: 337px; padding: 0 22px; }
  .bubble-mature { left: 322px; top: 522px; }

  .case-label {
    position: absolute; color: var(--ink); font-weight: 700; font-size: 22px; line-height: 1.25; white-space: nowrap;
  }
  .label-startup { left: 135px; top: 447px; }
  .label-challenge { left: 518px; top: 262px; }
  .label-mature { right: 648px; top: 577px; text-align: center; }

  .band {
    position: absolute; left: 34px; width: 772px;
    background: linear-gradient(90deg, var(--gold-dark) 0%, var(--gold-light) 100%);
    color: var(--white);
  }
  .band-benefits { top: 804px; height: 107px; }
  .band-training { top: 933px; height: 250px; }

  .band-heading { position: absolute; font-weight: 700; font-size: 28px; line-height: 1.2; text-align: center; }
  .benefits-heading { left: 143px; top: 41px; transform: translateY(-50%); }
  .training-heading { left: 141px; top: 48px; transform: translateX(-50%); white-space: nowrap; }

  .benefits-icon { position: absolute; left: 38px; top: 16px; width: 72px; height: 72px; border-radius: 50%; background: rgba(255,255,255,0.9); }
  .tools-icon { position: absolute; left: 110px; top: 140px; width: 60px; height: 60px; }

  .band-list { position: absolute; list-style: none; font-weight: 300; font-size: 16px; }
  .benefits-list { left: 330px; top: 26px; }
  .benefits-list li { position: relative; padding-left: 26px; height: 34px; line-height: 22px; }
  .benefits-list li::before {
    content: ""; position: absolute; left: 2px; top: 6px; width: 8px; height: 10px;
    border-radius: 40% 40% 50% 50%; background: var(--white);
  }
  .training-list { left: 300px; top: 36px; }
  .training-list li { position: relative; padding-left: 42px; line-height: 34.5px; }
  .training-list li::before {
    content: ""; position: absolute; left: 0; top: 11px; width: 12px; height: 12px;
    border: 1.5px solid var(--white);
  }
  .training-list .continued { padding-left: 44px; }
  .training-list .continued::before { display: none; }
</style>
</head>
<body>
<main class="flyer">
  <header class="hero" role="img" aria-label="Glowing blue network globe on a dark background">
    <svg class="hero-wave" viewBox="0 0 848 100" preserveAspectRatio="none">
      <path d="M0 38 C 90 20, 200 8, 290 16 C 430 30, 560 95, 848 96 L848 100 L0 100 Z" fill="var(--paper)"/>
    </svg>
    <h1 class="hero-title">AI, Blockchain, e-commerce</h1>
  </header>

  <svg class="connectors" viewBox="0 0 848 800">
    <g fill="none" stroke="var(--teal-dark)" stroke-width="3">
      <polyline points="138,304 39,378 99,451"/>
      <polyline points="489,276 446,356 543,440"/>
      <polyline points="223,611 263,739 336,711"/>
    </g>
    <g fill="var(--teal)">
      <rect x="96" y="447" width="26" height="26" rx="3" transform="rotate(45 109 460)"/>
      <rect x="476" y="263" width="26" height="26" rx="3" transform="rotate(45 489 276)"/>
      <rect x="210" y="598" width="26" height="26" rx="3" transform="rotate(45 223 611)"/>
    </g>
  </svg>

  <div class="case-bubble bubble-startup">You have a disruptive idea that needs an accelerator/incub ator program</div>
  <div class="case-bubble bubble-challenge">You want to solve an business problem but do not own an idea</div>
  <div class="case-bubble bubble-mature">You Have a Disruptive idea that needs a direct commercialization</div>

  <p class="case-label label-startup">Startup Idea</p>
  <p class="case-label label-challenge">Business Challenge</p>
  <p class="case-label label-mature">Mature<br>startup Idea</p>

  <section class="band band-benefits">
    <div class="benefits-icon" role="img" aria-label="Piggy bank savings icon"></div>
    <h2 class="band-heading benefits-heading">Benefits</h2>
    <ul class="band-list benefits-list">
      <li>Market and Investor Acces</li>
      <li>Direct access to all Partners</li>
    </ul>
  </section>

  <section class="band band-training">
    <h2 class="band-heading training-heading">Training<br>and Tools</h2>
    <svg class="tools-icon" viewBox="0 0 60 60" aria-label="Tools icon" role="img">
      <g stroke="var(--white)" stroke-linecap="round" fill="none">
        <line x1="10" y1="10" x2="50" y2="52" stroke-width="8"/>
        <line x1="50" y1="8" x2="12" y2="50" stroke-width="8"/>
      </g>
      <circle cx="10" cy="10" r="8" fill="var(--gold-dark)" stroke="var(--white)" stroke-width="4"/>
    </svg>
    <ul class="band-list training-list">
      <li>Mentor and Network Muscle</li>
      <li>We can link you to many domains like Sales,</li>
      <li class="continued">Marketing, Aftersales, IT und HR.</li>
      <li>Experiences Senior and University mentors.</li>
      <li>With all Partners as your first potential customer.</li>
    </ul>
  </section>
</main>
</body>
</html>
```